Creative, Fun, Eye catching signage for new office - inspire and inform!

I am looking for a billboard sign, a smaller sign and a very small sign for parking spots. These will be located in our new office space. I have uploaded two logos, this way you can choose. I would love to see what it looks like with black behind the logo but am open to creative ideas. I would like the majority of the background to be black and/or white

1. Sign for over door – with five at the top like in the photo attached

The sign size is 2600mm (L) x 900mm (H)

Logo at the top then services to the right side
Social & Living Skills Programs
Support Workers
Respite/Supported Holidays
Exercise Physiology
Occupational Therapy
Speech Therapy
Psychology
Behavioural Therapy

I would like the design to tie in with the website and/or flyers/banners attached. Please also try and add 1800 527 930

2. Sign for glass roller door

745cm wide by 725cm high ( similar to what next door has without it saying parent )

Tallbrook Logo
Drop Off Zone

Smaller signs for parking spots
1000cm wide, 60cm high

Tallbrook logo Visitor Parking 24/7

I would like the design to be consistent across the three items so they work together but are not identical.

I have attached images showing what I am talking about in relation to the location of each sign.

Target Market(s)

Families, parents and people with disabilities

Industry/Entity Type

Disability and community service

Colors

Designer to choose colors to be used in the design.

Requirements
Must have
• White or black background - the logo and please use colours shown in the brochures and banners provided. Preferences are black white and yellow
Nice to have
• all of our services and website and/or 1800 527 930 on banner 1
Should not have
• I dont want it to be to busy please

```html
<!DOCTYPE html>
<html lang="en">
<head>
<meta charset="utf-8">
<title>Tallbrook Signage Set</title>
<link href="https://fonts.googleapis.com/css2?family=Montserrat:ital,wght@0,600;0,700;0,800;1,800;1,900&display=swap" rel="stylesheet">
<style>
  :root {
    --ink: #000000;
    --paper: #ffffff;
    --rose: #e6416b;
    --sun: #f2cf4a;
    --shadow: rgba(0, 0, 0, 0.35);
  }
  * { margin: 0; padding: 0; box-sizing: border-box; }
  html, body {
    width: 1200px;
    height: 575px;
    overflow: hidden;
    background: var(--paper);
    font-family: "Montserrat", Arial, sans-serif;
  }
  .canvas {
    position: relative;
    width: 1200px;
    height: 575px;
  }
  .sign {
    position: absolute;
    background: var(--ink);
    overflow: hidden;
    box-shadow: 2px 3px 3px var(--shadow);
  }
  .sign-art {
    position: absolute;
    inset: 0;
    width: 100%;
    height: 100%;
  }
  .sun-dot {
    position: absolute;
    border-radius: 50%;
    background: var(--sun);
  }
  .brand-name {
    position: absolute;
    color: var(--paper);
    font-weight: 700;
    white-space: nowrap;
    transform: translateX(-50%);
    line-height: 1;
  }

  /* Parking strip */
  .parking-strip { left: 24px; top: 94px; width: 1154px; height: 71px; }
  .parking-strip .sun-dot { left: 132px; top: 6px; width: 24px; height: 24px; }
  .parking-strip .brand-name { left: 144px; top: 36px; font-size: 21px; }
  .parking-title {
    position: absolute;
    left: 537px;
    top: 4px;
    transform: translateX(-50%);
    color: var(--paper);
    font-weight: 900;
    font-style: italic;
    font-size: 56px;
    line-height: 1.1;
    white-space: nowrap;
  }
  .parking-hours {
    position: absolute;
    left: 1005px;
    top: 10px;
    transform: translateX(-50%);
    color: var(--paper);
    font-weight: 800;
    font-size: 46px;
    line-height: 1.1;
  }

  /* Door sign */
  .door-sign { left: 24px; top: 176px; width: 824px; height: 285px; }
  .door-sign .sun-dot { left: 272px; top: 24px; width: 90px; height: 90px; }
  .door-sign .brand-name { left: 244px; top: 148px; font-size: 74px; }
  .door-web {
    position: absolute;
    left: 34px;
    top: 255px;
    color: var(--paper);
    font-weight: 700;
    font-size: 16px;
    line-height: 1;
  }
  .service-list {
    position: absolute;
    left: 703px;
    top: 72px;
    transform: translateX(-50%);
    list-style: none;
    text-align: center;
    color: var(--paper);
    font-weight: 800;
    font-size: 12.5px;
    line-height: 16px;
    white-space: nowrap;
  }
  .door-phone {
    position: absolute;
    left: 703px;
    top: 214px;
    transform: translateX(-50%);
    color: var(--paper);
    font-weight: 800;
    font-size: 31px;
    line-height: 1;
    white-space: nowrap;
  }

  /* Drop-off sign */
  .dropoff-sign { left: 878px; top: 176px; width: 300px; height: 286px; }
  .dropoff-sign .sun-dot { left: 159px; top: 9px; width: 42px; height: 42px; }
  .dropoff-sign .brand-name { left: 150px; top: 66px; font-size: 37px; }
  .dropoff-label {
    position: absolute;
    left: 150px;
    top: 212px;
    transform: translateX(-50%);
    text-align: center;
    color: var(--paper);
    font-weight: 800;
    font-size: 27px;
    line-height: 1.05;
    white-space: nowrap;
  }
</style>
</head>
<body>
<main class="canvas">

  <section class="sign parking-strip">
    <svg class="sign-art" viewBox="0 0 1154 71" preserveAspectRatio="none" role="img" aria-label="Rose burst shape sweeping in from the right">
      <polygon points="840,0 1154,0 1154,71 884,71 944,35" fill="var(--rose)"/>
      <rect x="810" y="18" width="160" height="33" rx="16.5" fill="var(--rose)"/>
    </svg>
    <span class="sun-dot"></span>
    <span class="brand-name">Tallbrook</span>
    <h1 class="parking-title">Visitor Parking</h1>
    <span class="parking-hours">24/7</span>
  </section>

  <section class="sign door-sign">
    <svg class="sign-art" viewBox="0 0 824 285" preserveAspectRatio="none" role="img" aria-label="Rose burst panel behind the services list">
      <path d="M522,0 C486,70 470,110 474,145 C478,185 494,230 530,285 L824,285 L824,0 Z" fill="var(--rose)"/>
    </svg>
    <span class="sun-dot"></span>
    <span class="brand-name">Tallbrook</span>
    <span class="door-web">www.tallbrook.com.au</span>
    <ul class="service-list">
      <li>Social &amp; Living Skills Programs</li>
      <li>Support Workers</li>
      <li>Respite/Supported Holidays</li>
      <li>Exercise Physiology</li>
      <li>Occupational Therapy</li>
      <li>Speech Therapy</li>
      <li>Psychology</li>
      <li>Behavioural Therapy</li>
    </ul>
    <span class="door-phone">1800 527 930</span>
  </section>

  <section class="sign dropoff-sign">
    <svg class="sign-art" viewBox="0 0 300 286" preserveAspectRatio="none" role="img" aria-label="Rose burst rising from the bottom edge">
      <path d="M-40,286 A190,176 0 0 1 340,286 Z" fill="var(--rose)"/>
    </svg>
    <span class="sun-dot"></span>
    <span class="brand-name">Tallbrook</span>
    <p class="dropoff-label">Drop-Off<br>Zone</p>
  </section>

</main>
</body>
</html>
```